Business card design for international hub site

I need a business card design with the logo attached. Although the site is for the teenage audience (it is about the high school graduation ball, the Prom), the business card is for professional use to be given to professional contacts (B2B), such as suppliers and partners, so it needs to look professional (but also girly, glamours and clean).

Target Market(s)

B2B

Industry/Entity Type

Media

Colors
eea4c8
f9d9e8
e667a6
9d9d9d
1b1b1b

Requirements
Must have
• Space for Name, Tile, Address, Phone, email and website.
Should not have
• Photo

```html
<!DOCTYPE html>
<html lang="en">
<head>
<meta charset="utf-8">
<title>The Gala Hive – Business Card</title>
<link rel="stylesheet" href="https://fonts.googleapis.com/css2?family=EB+Garamond:wght@400;600&family=Pinyon+Script&display=swap">
<style>
  :root {
    --page-bg: #ececec;
    --ink-dark: #1b1b1b;
    --ink-dark-soft: #2c2c2c;
    --paper: #ffffff;
    --paper-soft: #efefef;
    --pink: #e667a6;
    --pink-bright: #f06aa8;
    --pink-light: #eea4c8;
    --grey: #9d9d9d;
    --text-dark: #1b1b1b;
    --text-light: #ffffff;
  }
  * { box-sizing: border-box; margin: 0; padding: 0; }
  html, body {
    width: 1200px;
    height: 586px;
    overflow: hidden;
    background: var(--page-bg);
  }
  .canvas {
    position: relative;
    width: 1200px;
    height: 586px;
  }
  .card {
    position: absolute;
    top: 123px;
    width: 502px;
    height: 301px;
    overflow: hidden;
  }
  .card--front { left: 65px; }
  .card--back { left: 608px; }

  .card__texture {
    position: absolute;
    inset: 0;
  }
  .card--front .card__texture {
    background: linear-gradient(135deg, var(--ink-dark-soft) 0%, var(--ink-dark) 55%, #232323 100%);
  }
  .card--back .card__texture {
    background: linear-gradient(160deg, var(--paper-soft) 0%, var(--paper) 45%, #e8e8e8 100%);
  }

  /* Front */
  .brand-name {
    position: absolute;
    left: 0;
    right: 0;
    top: 78px;
    text-align: center;
    font-family: "EB Garamond", Georgia, serif;
    font-weight: 400;
    font-size: 52px;
    line-height: 1;
    color: var(--text-light);
    letter-spacing: 0.5px;
  }
  .website {
    position: absolute;
    left: 0;
    right: 0;
    top: 258px;
    text-align: center;
    font-family: "EB Garamond", Georgia, serif;
    font-weight: 600;
    font-size: 11.5px;
    letter-spacing: 3.2px;
    color: var(--text-light);
  }

  /* Back */
  .person-name {
    position: absolute;
    left: 58px;
    top: 134px;
    font-family: "Pinyon Script", cursive;
    font-size: 31px;
    line-height: 1.2;
    color: var(--text-dark);
    white-space: nowrap;
  }
  .divider {
    position: absolute;
    left: 251px;
    top: 86px;
    width: 2px;
    height: 134px;
    background: linear-gradient(to bottom, rgba(230,103,166,0) 0%, var(--pink) 25%, var(--pink) 75%, rgba(230,103,166,0) 100%);
  }
  .contact-list {
    position: absolute;
    left: 277px;
    top: 121px;
    list-style: none;
  }
  .contact-list__item {
    display: flex;
    align-items: center;
    height: 24.5px;
    font-family: "EB Garamond", Georgia, serif;
    font-size: 12.5px;
    color: var(--text-dark);
    white-space: nowrap;
  }
  .contact-list__icon {
    width: 13px;
    height: 11px;
    margin-right: 9px;
    fill: var(--pink-bright);
    flex: none;
  }
  .address {
    position: absolute;
    left: 0;
    right: 0;
    top: 270px;
    text-align: center;
    font-family: "EB Garamond", Georgia, serif;
    font-size: 13.5px;
    color: var(--pink-bright);
  }
</style>
</head>
<body>
<main class="canvas">
  <section class="card card--front">
    <div class="card__texture" role="img" aria-label="Dark faceted polygon texture"></div>
    <p class="brand-name">the gala hive</p>
    <p class="website">www.thegalahive.com</p>
  </section>

  <section class="card card--back">
    <div class="card__texture" role="img" aria-label="White faceted polygon texture"></div>
    <h1 class="person-name">Mara Lindqvist</h1>
    <span class="divider"></span>
    <ul class="contact-list">
      <li class="contact-list__item">
        <svg class="contact-list__icon" viewBox="0 0 13 11" aria-hidden="true">
          <path d="M0.5 3.2 C2 0.6 11 0.6 12.5 3.2 L12.5 4.4 L9.6 4.4 L9.3 3.2 L3.7 3.2 L3.4 4.4 L0.5 4.4 Z"/>
          <path d="M3.2 5 L9.8 5 L11.6 10.5 L1.4 10.5 Z"/>
        </svg>
        +44 (0)1632 960418
      </li>
      <li class="contact-list__item">
        <svg class="contact-list__icon" viewBox="0 0 13 11" aria-hidden="true">
          <rect x="3" y="0.5" width="7" height="3"/>
          <path d="M0.5 4 H12.5 V8.5 H10.5 V6.5 H2.5 V8.5 H0.5 Z"/>
          <rect x="3" y="7.2" width="7" height="3.3"/>
        </svg>
        (555) 014-2287
      </li>
      <li class="contact-list__item">
        <svg class="contact-list__icon" viewBox="0 0 13 11" aria-hidden="true">
          <path d="M0.5 1.5 H12.5 L6.5 6.2 Z"/>
          <path d="M0.5 2.8 L6.5 7.6 L12.5 2.8 V10 H0.5 Z"/>
        </svg>
        hello@thegalahive.com
      </li>
    </ul>
    <p class="address">Elm Court, Ashby Vale, AV4 2QT</p>
  </section>
</main>
</body>
</html>
```